Lumora Business Card Design

hello,
we are looking for a business card design for our Fintech Company. We are credit card processing company that is also expanding in to the crypto market. We will be focusing on crypto processing, with a crypto wallet and crypto exchange. We like the purple in the logo. We want something modern and sophisticated but at the same time simple and trust worthy to work with banks.

Industry/Entity Type

Fintech

Logo Text

Lumora

```html
<!DOCTYPE html>
<html lang="en">
<head>
<meta charset="utf-8">
<title>Lumora Business Card</title>
<link href="https://fonts.googleapis.com/css2?family=Roboto+Condensed:wght@500;700&display=swap" rel="stylesheet">
<style>
  :root {
    --page-bg: #4a4a4a;
    --card-bg: #ffffff;
    --navy: #22325a;
    --violet: #4b33b8;
    --violet-light: #8f7af5;
    --slate-light: #7f93ba;
    --slate-dark: #34466f;
  }
  html, body {
    margin: 0;
    width: 1200px;
    height: 800px;
    overflow: hidden;
    background: var(--page-bg);
    font-family: "Roboto Condensed", "Arial Narrow", sans-serif;
  }
  .canvas {
    position: relative;
    width: 1200px;
    height: 800px;
  }
  .card {
    position: absolute;
    width: 533px;
    height: 329px;
    background: var(--card-bg);
    overflow: hidden;
  }
  .card--front { left: 49px; top: 83px; }
  .card--back { left: 621px; top: 335px; }
  .card__shapes {
    position: absolute;
    inset: 0;
    width: 100%;
    height: 100%;
  }
  .wordmark {
    position: absolute;
    margin: 0;
    font-weight: 700;
    color: var(--navy);
    letter-spacing: -1px;
    line-height: 1;
  }
  .card--front .wordmark {
    left: 0;
    right: 0;
    top: 135px;
    text-align: center;
    font-size: 60px;
  }
  .card--back .wordmark {
    right: 25px;
    top: 16px;
    font-size: 44px;
  }
  .contact {
    position: absolute;
    right: 25px;
    bottom: 25px;
    text-align: right;
  }
  .contact__name {
    margin: 0;
    font-size: 34px;
    font-weight: 700;
    color: var(--violet);
    line-height: 1.05;
  }
  .contact__role {
    margin: 4px 0 18px;
    font-size: 18px;
    font-weight: 700;
    color: var(--violet);
    text-transform: uppercase;
  }
  .contact__lines {
    margin: 0;
    font-size: 13px;
    font-weight: 700;
    color: var(--navy);
    line-height: 1.3;
  }
</style>
</head>
<body>
<main class="canvas">

  <section class="card card--front" aria-label="Card front">
    <svg class="card__shapes" viewBox="0 0 400 247" preserveAspectRatio="none" aria-hidden="true">
      <defs>
        <linearGradient id="frontSlate" x1="0" y1="0" x2="1" y2="0">
          <stop offset="0" stop-color="var(--slate-light)"/>
          <stop offset="1" stop-color="var(--slate-dark)"/>
        </linearGradient>
        <linearGradient id="frontViolet" x1="0" y1="0" x2="1" y2="0">
          <stop offset="0" stop-color="var(--violet-light)"/>
          <stop offset="1" stop-color="var(--violet)"/>
        </linearGradient>
        <linearGradient id="cornerViolet" x1="0" y1="0" x2="1" y2="1">
          <stop offset="0" stop-color="var(--violet-light)"/>
          <stop offset="1" stop-color="var(--violet)"/>
        </linearGradient>
      </defs>
      <polygon points="0,0 232,0 12,66 0,70" fill="url(#frontSlate)"/>
      <polygon points="0,0 12,0 12,66 0,70" fill="var(--violet)" opacity="0.8"/>
      <polygon points="0,70 12,66 48,247 0,247" fill="url(#frontViolet)"/>
      <polygon points="348,0 400,0 400,124 383,135" fill="var(--slate-dark)"/>
      <polygon points="270,247 400,122 400,247" fill="url(#cornerViolet)"/>
    </svg>
    <h1 class="wordmark">Lumora</h1>
  </section>

  <section class="card card--back" aria-label="Card back">
    <svg class="card__shapes" viewBox="0 0 400 247" preserveAspectRatio="none" aria-hidden="true">
      <defs>
        <linearGradient id="backSlate" x1="0" y1="0" x2="1" y2="0">
          <stop offset="0" stop-color="var(--slate-light)"/>
          <stop offset="1" stop-color="var(--navy)"/>
        </linearGradient>
        <linearGradient id="backViolet" x1="0" y1="1" x2="1" y2="0">
          <stop offset="0" stop-color="var(--violet-light)"/>
          <stop offset="1" stop-color="#6a52dc"/>
        </linearGradient>
      </defs>
      <polygon points="0,0 212,0 60,178 0,136" fill="url(#backSlate)"/>
      <polygon points="0,136 60,178 0,247" fill="var(--violet)"/>
      <polygon points="60,178 158,247 0,247" fill="url(#backViolet)"/>
    </svg>
    <h2 class="wordmark">Lumora</h2>
    <div class="contact">
      <p class="contact__name">Name Example</p>
      <p class="contact__role">Job Title</p>
      <p class="contact__lines">111 2222 3333<br>hello@lumorapay.com<br>www.lumorapay.com</p>
    </div>
  </section>

</main>
</body>
</html>
```